Need A Homepage Redesign For Ecommerce Store

Just looking for a great quality designer to redesign my homepage. We will take current structure and redesign to make it cleaner and more user friendly.

Our website is here - www.brivonelfilters.com

Please see the attached for the layout structure that we would like. Please be creative as well.

As you can see the current design does not look clean and is not user friendly.

See attached and thank you and good luck!

P.S. Whoever wins I will give them the next work for product pages and other landing pages.

Target Market(s)

Middle to upper class health minded people, ages 30 and up

Industry/Entity Type

Health And Wellness

Number of Pages Required

1 page

Font styles to use
Sans Serif

Colors
0255a3
0792cd
00a990

Requirements
Must have
• Clean design. Professional design. Use current logo and tagline (unless you think you can do better).
Nice to have
• I would like to see some creativity as well.
Should not have
• Please dont use the same structure as I have. Want this to be a total redesign.

```html
<!DOCTYPE html>
<html lang="en">
<head>
<meta charset="utf-8">
<title>Brivonel Water Ionizers – Home</title>
<link href="https://fonts.googleapis.com/css2?family=Raleway:wght@400;500;600;700&family=Open+Sans:wght@400;600&display=swap" rel="stylesheet">
<style>
:root{
  --brand-blue:#0255a3;
  --sky:#0792cd;
  --teal:#00a990;
  --teal-panel:#3aa88e;
  --ink:#333;
  --footer:#3a3a3a;
  --footer-bottom:#2e2e2e;
  --white:#fff;
  --line:#d8d8d8;
}
*{box-sizing:border-box;margin:0;padding:0}
html,body{width:1200px;height:2564px;overflow:hidden;background:var(--white)}
body{font-family:"Open Sans",Arial,sans-serif;color:var(--ink);position:relative}
.abs{position:absolute}
.brand{display:flex;align-items:center;gap:10px}
.brand-dot{width:40px;height:40px;border-radius:50%;background:var(--sky)}
.brand-name{font-family:"Raleway",Arial,sans-serif;font-weight:700;color:var(--sky);font-size:28px;letter-spacing:.5px}

/* header */
.site-header{top:0;left:0;width:1200px;height:77px;background:var(--white)}
.header-logo{left:100px;top:18px}
.utility{right:110px;top:28px;display:flex;gap:44px;font-size:13px;color:#444}
.utility span{display:flex;align-items:center;gap:8px}
.main-nav{top:77px;left:0;width:1200px;height:51px;background:var(--brand-blue);display:flex;justify-content:center}
.main-nav a{color:var(--white);text-decoration:none;font-size:13px;line-height:51px;padding:0 38px;position:relative}
.main-nav a.active::after{content:"";position:absolute;left:32px;right:32px;bottom:0;height:4px;background:var(--white)}

/* hero */
.hero{top:128px;left:0;width:1200px;height:398px;background:linear-gradient(160deg,#e4ecf2 0%,#b7c9d8 40%,#8ea8be 70%,#c9d6e0 100%)}
.hero-logo{left:236px;top:50px}
.hero-logo .brand-name{color:var(--white)}
.hero-logo .brand-dot{background:rgba(255,255,255,.85)}
.hero-copy{left:96px;top:140px;width:530px;text-align:center;color:var(--white);font-family:"Raleway",Arial,sans-serif}
.hero-copy .sale{font-size:25px;font-weight:600}
.hero-copy .sub{font-size:25px;font-weight:400;margin-top:12px}
.hero-copy .code{font-size:29px;font-weight:700;margin-top:14px}
.hero-btn{display:inline-block;margin-top:22px;border:2px solid var(--white);border-radius:6px;padding:8px 22px;font-size:21px}
.quote{left:730px;top:21px;width:369px;height:355px;background:var(--white);border:1px solid #ccc;padding:16px 34px}
.quote h2{font-family:"Raleway",Arial,sans-serif;font-size:25px;font-weight:600;color:#222;text-align:center}
.quote .start{text-align:center;color:var(--brand-blue);font-size:14px;margin:8px 0 18px}
.field{height:41px;border:1px solid #bbb;border-radius:2px;margin-bottom:8px;font-size:13px;color:#aaa;padding:11px 12px;position:relative}
.send{width:112px;height:33px;margin:14px auto 0;background:var(--brand-blue);color:var(--white);text-align:center;line-height:33px;font-weight:600;font-size:15px;border-radius:2px}
.close{right:8px;top:4px;font-size:13px;color:#777}

/* section titles */
.section-title{display:flex;align-items:center;justify-content:center;gap:14px;font-family:"Raleway",Arial,sans-serif;font-size:26px;font-weight:500;color:var(--brand-blue)}
.title-dot{width:34px;height:34px;border-radius:50%;border:3px solid var(--sky);background:#dff1fa}

/* products */
.products-title{top:562px;left:0;width:1200px}
.card{top:643px;width:300px;height:280px;border:1px solid var(--line);background:var(--white);overflow:hidden}
.card-label{text-align:center;font-family:"Raleway",Arial,sans-serif;color:var(--brand-blue);font-size:16px;font-weight:600;margin-top:12px}
.card-media{position:absolute;left:50px;top:44px;width:200px;height:150px;border-radius:6px}
.card-foot{position:absolute;left:0;bottom:0;width:300px;height:102px}
.card-name{position:absolute;bottom:14px;width:100%;text-align:center;color:var(--white);font-family:"Raleway",Arial,sans-serif;font-size:18px;font-weight:500}

/* split */
.split-left{top:969px;left:0;width:600px;height:333px;background:var(--teal-panel);color:var(--white)}
.split-right{top:969px;left:600px;width:600px;height:333px;background:linear-gradient(180deg,#2a527f,#3a6d9f);color:var(--white)}
.avatar{left:100px;top:36px;width:104px;height:104px;border-radius:50%;background:linear-gradient(150deg,#b9c8d6,#7b8a98);border:3px solid rgba(255,255,255,.6)}
.split h3{font-family:"Raleway",Arial,sans-serif;font-weight:500;font-size:21px;line-height:1.5}
.split p{font-size:13px;line-height:2.05}
.split a{color:var(--white);font-size:13px;text-decoration:underline}
.divider-dot{left:584px;top:1120px;width:32px;height:32px;border-radius:50%;background:var(--white);border:3px solid var(--teal)}

/* confidence */
.confidence{top:1302px;left:0;width:1200px;height:723px;background:linear-gradient(150deg,#474747 0%,#3a3a3a 40%,#2f3a48 70%,#404040 100%);color:var(--white)}
.confidence .section-title{color:var(--white);position:absolute;top:60px;width:1200px;font-weight:600}
.badge{border-radius:50%;background:#555}
.badge-inner{position:absolute;border-radius:50%;background:linear-gradient(145deg,#f2cf5a,#b8860b)}
.conf-text{font-size:15px;line-height:2}
.conf-text b{font-weight:600;font-size:16px}

/* resources */
.resources{top:2025px;left:0;width:1200px;height:219px}
.resources .section-title{position:absolute;top:40px;width:1200px}
.resources p{position:absolute;top:106px;left:130px;width:940px;text-align:center;font-size:12px;line-height:2.45;color:#555}

/* footer */
.footer{top:2244px;left:0;width:1200px;height:246px;background:var(--footer);color:#ddd}
.footer h4{font-family:"Raleway",Arial,sans-serif;font-size:15px;font-weight:600;color:var(--white);letter-spacing:.5px}
.footer ul{list-style:none;margin-top:20px}
.footer li{font-size:12px;line-height:27.5px;color:#ddd}
.footer li::before{content:"›";font-weight:700;margin-right:10px}
.contact-row{display:flex;gap:14px;font-size:12px;line-height:1.6;margin-top:16px}
.social{display:flex;gap:10px;margin-top:22px}
.social span{width:38px;height:38px;border-radius:50%;border:2px solid var(--white)}
.footer-bottom{top:2490px;left:0;width:1200px;height:74px;background:var(--footer-bottom);color:#ddd;font-size:12px;text-align:center;line-height:74px}
</style>
</head>
<body>

<header class="site-header abs">
  <div class="header-logo abs">
    <div class="brand"><span class="brand-dot"></span><span class="brand-name">BRIVONEL</span></div>
  </div>
  <div class="utility abs">
    <span><svg width="18" height="18" viewBox="0 0 18 18"><rect x="6" y="2" width="10" height="14" fill="none" stroke="#0aa98d" stroke-width="2"/><path d="M1 9h9M7 6l3 3-3 3" fill="none" stroke="#0aa98d" stroke-width="2"/></svg>Log in</span>
    <span><svg width="18" height="18" viewBox="0 0 18 18"><circle cx="9" cy="9" r="8" fill="#0aa98d"/><circle cx="9" cy="7" r="3" fill="#fff"/><path d="M4 14c2-3 8-3 10 0" fill="#fff"/></svg>My Account</span>
    <span><svg width="18" height="18" viewBox="0 0 18 18"><path d="M1 3h3l2 8h9l2-6H5" fill="none" stroke="#0aa98d" stroke-width="1.6"/><circle cx="7" cy="15" r="1.5" fill="#0aa98d"/><circle cx="14" cy="15" r="1.5" fill="#0aa98d"/></svg>Cart</span>
    <span><svg width="18" height="18" viewBox="0 0 18 18"><circle cx="9" cy="9" r="8" fill="none" stroke="#0aa98d" stroke-width="1.6"/><text x="9" y="13" text-anchor="middle" font-size="11" fill="#0aa98d" font-family="Arial">?</text></svg>Help</span>
  </div>
</header>

<nav class="main-nav abs">
  <a class="active">Home</a><a>Browse Products</a><a>Why Brivonel?</a><a>Compare</a><a>Support</a><a>Water Ionizer Info</a><a>Testimonials</a>
</nav>

<section class="hero abs" role="img" aria-label="Splash of clear blue water across a light background">
  <svg class="abs" style="left:44px;top:178px" width="24" height="44" viewBox="0 0 24 44"><path d="M20 2L4 22l16 20" fill="none" stroke="#fff" stroke-width="2"/></svg>
  <svg class="abs" style="right:44px;top:178px" width="24" height="44" viewBox="0 0 24 44"><path d="M4 2l16 20L4 42" fill="none" stroke="#fff" stroke-width="2"/></svg>
  <div class="hero-logo abs">
    <div class="brand"><span class="brand-dot"></span><span class="brand-name">BRIVONEL</span></div>
  </div>
  <div class="hero-copy abs">
    <div class="sale">20% Off Super Summer Sale Going On Now</div>
    <div class="sub">Start Enjoying The Power Of Brivonel</div>
    <div class="code">Use Coupon Code 20Off</div>
    <div class="hero-btn">Click Here To Shop</div>
  </div>
  <form class="quote abs">
    <span class="close abs">x</span>
    <h2>Get Instant Online Quote</h2>
    <div class="start">Start Here Now</div>
    <div class="field">Name</div>
    <div class="field">Mobile</div>
    <div class="field">Email</div>
    <div class="field">Solution Requested<svg class="abs" style="right:10px;top:16px" width="10" height="6" viewBox="0 0 10 6"><path d="M1 1l4 4 4-4" fill="none" stroke="#777" stroke-width="1.4"/></svg></div>
    <div class="send">Send</div>
  </form>
</section>

<div class="products-title abs"><div class="section-title"><span class="title-dot"></span>Shop Water Ionizers</div></div>

<article class="card abs" style="left:120px">
  <div class="card-label">Our Best Seller</div>
  <div class="card-media" role="img" aria-label="Silver countertop water ionizer with display panel and spout" style="background:linear-gradient(160deg,#eceff2,#b9c0c7)"></div>
  <svg class="card-foot" viewBox="0 0 300 102"><polygon points="0,14 150,54 300,14 300,102 0,102" fill="#0255a3"/><circle cx="150" cy="54" r="12" fill="#fff"/><circle cx="150" cy="54" r="7" fill="#0792cd"/></svg>
  <div class="card-name">Brivonel Crestline Ionizer</div>
</article>
<article class="card abs" style="left:451px">
  <div class="card-label">Perfect in Between Machine</div>
  <div class="card-media" role="img" aria-label="Grey countertop water ionizer with display panel and spout" style="background:linear-gradient(160deg,#e6e9ec,#a9b1b9)"></div>
  <svg class="card-foot" viewBox="0 0 300 102"><polygon points="0,14 150,54 300,14 300,102 0,102" fill="#0255a3"/><circle cx="150" cy="54" r="12" fill="#fff"/><circle cx="150" cy="54" r="7" fill="#0792cd"/></svg>
  <div class="card-name">Brivonel Harbor Ionizer</div>
</article>
<article class="card abs" style="left:786px">
  <div class="card-label">Our Super Saver</div>
  <div class="card-media" role="img" aria-label="Black and silver countertop water ionizer with spout" style="background:linear-gradient(160deg,#d8dadd,#2a2a2a)"></div>
  <svg class="card-foot" viewBox="0 0 300 102"><polygon points="0,14 150,54 300,14 300,102 0,102" fill="#0255a3"/><circle cx="150" cy="54" r="12" fill="#fff"/><circle cx="150" cy="54" r="7" fill="#0792cd"/></svg>
  <div class="card-name">Brivonel Riptide Ionizer</div>
</article>

<section class="split split-left abs">
  <div class="avatar abs" role="img" aria-label="Portrait of a smiling customer"></div>
  <h3 class="abs" style="left:232px;top:56px;width:330px">What Are People Saying About<br>&nbsp;Brivonel Water Ionizers?</h3>
  <p class="abs" style="left:100px;top:158px;width:460px">For the quality of this water ionizer , I would have expected to pay double what i ended up paying for . Customer service was amazing . Highly recommended</p>
  <a class="abs" style="right:42px;top:271px">Click Here to see why are #1</a>
</section>
<section class="split split-right abs">
  <h3 class="abs" style="left:42px;top:56px">Find The Right Water Ionizer For You</h3>
  <p class="abs" style="left:42px;top:102px;width:460px;font-size:12px;line-height:2.1">Quo ad viris appareat erroribus. Mea appetere sapientem efficiendi ut, te sit veritus deterruisset. Duo nobis patrioque ad, et eum percipit liberavisse. Mutat ridens ex quiQuo ad viris appareat erroribus. Mea appetere sapientem efficiendi ut, te sit veritus deterruisset. Duo nobis patrioque ad, et eum percipit liberavisse. Mutat ridens ex quiDuo nobis patrioque ad, et eum percipit liberavisse.</p>
  <a class="abs" style="right:98px;top:271px">Compare Water Ionizer</a>
</section>
<div class="divider-dot abs"></div>

<section class="confidence abs" role="region" aria-label="Shop with confidence">
  <div class="section-title"><span class="title-dot" style="width:28px;height:28px"></span>Shop With Confidence - Our Water Ionizers Are Simply the best !</div>
  <div class="badge abs" style="left:206px;top:135px;width:196px;height:196px"><div class="badge-inner" style="left:22px;top:22px;width:152px;height:152px"></div></div>
  <p class="conf-text abs" style="left:459px;top:210px;width:560px"><b>Quality - </b>Our Brivonel Water ionizers Are backed by Our Lifetime Warranty<br>&nbsp;We Will Ensure Your Water Ionizer Works For Life , Guaranteed!</p>
  <p class="conf-text abs" style="left:231px;top:368px;width:578px"><b>Still ensure ?</b> No Prblem yOu have 90 days to test our machines &amp; If for whatever reasonyou decise you dont love amazing alkaline water , simple return your water ionizer machine . we wont hassle youwe swear</p>
  <div class="badge abs" style="left:834px;top:300px;width:214px;height:214px"><div class="badge-inner" style="left:24px;top:24px;width:166px;height:166px"></div></div>
  <div class="badge abs" role="img" aria-label="Illustration of a support agent with headset at a computer" style="left:204px;top:490px;width:162px;height:162px;background:linear-gradient(150deg,#6a6a6a,#4a4f58)"></div>
  <p class="conf-text abs" style="left:459px;top:542px;width:650px">Rain or shine we always got your back . Our Promise is to give you the very best customer sevice Possible ! We will change the way you think about customer service after buying a water ionizer from us</p>
</section>

<section class="resources abs">
  <div class="section-title"><span class="title-dot"></span>Water Ionizer And Alkaline Water Resources</div>
  <p>Drinking Water From An Alkaline Water Machine Can Benefit You &amp; Your Family But How? Still not sure if Brivonel Ionizers are right for you? Try it and see for yourself.<br>If for whatever reason you decide you don't want to keep your Brivonel Water Ionizer, ship it back to us and we will give you a complete refund, no questions asked.<br>Can Benefit You &amp; Your Family But How? Still not sure if Brivonel Ionizers are right for you? Try it and see for yourself. If</p>
</section>

<footer class="footer abs">
  <div class="abs" style="left:98px;top:106px"><div class="brand"><span class="brand-dot"></span><span class="brand-name" style="font-size:26px">BRIVONEL</span></div></div>
  <div class="abs" style="left:355px;top:36px"><h4>MENUS</h4><ul><li>Home</li><li>About us</li><li>Our services</li><li>Blog</li><li>Contact us</li></ul></div>
  <div class="abs" style="left:498px;top:36px"><h4>QUICK LINKS</h4><ul><li>Site map</li><li>Terms and Conditions</li><li>Disclaimer</li><li>Privacy Policy</li><li>Contact us</li></ul></div>
  <div class="abs" style="left:693px;top:36px;width:210px">
    <h4>CONTACT US</h4>
    <div class="contact-row" style="margin-top:20px"><svg width="16" height="14" viewBox="0 0 16 14"><path d="M8 1L1 7h2v6h4V9h2v4h4V7h2z" fill="#fff"/></svg><span>2280 Larkfield Rd. | Dunmore<br>KS 66020</span></div>
    <div class="contact-row"><svg width="16" height="16" viewBox="0 0 16 16"><rect x="4" y="1" width="8" height="14" rx="1.5" fill="none" stroke="#fff" stroke-width="1.6"/></svg><span>Call Us : (555)010-3456</span></div>
    <div class="contact-row"><svg width="16" height="14" viewBox="0 0 16 14"><rect x="1" y="2" width="14" height="10" fill="none" stroke="#fff" stroke-width="1.5"/><path d="M1 2l7 6 7-6" fill="none" stroke="#fff" stroke-width="1.5"/></svg><span>info@brivonelfilters.com</span></div>
  </div>
  <div class="abs" style="left:922px;top:36px"><h4>CONNECT US WITH</h4><div class="social"><span></span><span></span><span></span><span></span></div></div>
</footer>
<div class="footer-bottom abs">© &nbsp;Companyname 2016 . All Rights Reserved</div>

</body>
</html>
```